Bramblecrest Real Estate

We are looking for help with web design for a new company that is revolutionizing the real estate world on the listing side: by charing per hour for top level professional real estate services. We would like the concept to be simple, clean and easily understood.
Updates

We want this website to actually function, not just a static design.

Industry/Entity Type

Real Estate

```html
<!DOCTYPE html>
<html lang="en">
<head>
<meta charset="utf-8">
<title>Bramblecrest Real Estate</title>
<link href="https://fonts.googleapis.com/css2?family=Open+Sans:wght@300;400;600&family=Cabin:wght@400;500;600&family=Oswald:wght@400;500&family=Arimo:wght@400&family=Roboto:wght@400&display=swap" rel="stylesheet">
<style>
:root{
  --brand-orange:#c98a45;
  --brand-beige:#e9d2b6;
  --headline-grey:#3a3a3a;
  --hero-red:#a8141b;
  --accent-red:#ec4b57;
  --text-grey:#8a8a8a;
  --text-rose:#b0636a;
  --rule:#e3e3e3;
  --ink:#111;
  --button-grey:#b8b8b8;
  --map-slate:#3d4659;
  --location-gold:#f0b323;
  --white:#fff;
}
*{margin:0;padding:0;box-sizing:border-box}
html,body{width:1200px;height:2211px;overflow:hidden;background:var(--white)}
body{position:relative;font-family:"Open Sans",sans-serif;color:var(--ink)}
.abs{position:absolute}

/* header */
.site-header{left:0;top:0;width:1200px;height:103px;background:linear-gradient(#f4f4f4,#fff);z-index:3}
.header-wedge{left:495px;top:0}
.brand-name{left:52px;top:86px;font-family:"Cabin",sans-serif;font-weight:600;font-size:17px;letter-spacing:2px;color:var(--brand-orange);text-transform:uppercase;line-height:1.3;width:170px}
.main-nav{left:0;top:0;width:1200px;height:103px}
.nav-item{position:absolute;top:0;height:103px;line-height:114px;font-family:"Cabin",sans-serif;font-weight:500;font-size:14px;color:var(--ink);text-decoration:none;text-align:center;width:120px;margin-left:-60px}
.nav-item.is-active{left:675px;width:103px;margin-left:-51px;background:var(--brand-orange);color:var(--white)}

/* hero */
.hero{left:0;top:103px;width:1200px;height:683px;background:linear-gradient(#fff 0%,#fafafa 60%,#f1f1f1 100%)}
.hero-visual{left:0;top:60px;width:860px;height:600px;background:radial-gradient(ellipse at 48% 55%,#d9d6d2 0%,#ebe7e2 40%,rgba(245,243,240,0) 72%)}
.hero-title{left:535px;top:52px;font-family:"Arimo",sans-serif;font-size:46px;letter-spacing:4px;color:var(--headline-grey);font-weight:400}
.hero-title-strong{left:718px;top:110px;font-family:"Cabin",sans-serif;font-weight:600;font-size:60px;color:var(--hero-red);letter-spacing:1px}
.hero-sub{left:843px;top:374px;font-family:"Oswald",sans-serif;font-weight:500;font-size:30px;color:var(--ink);letter-spacing:.3px}
.hero-sub span{color:var(--hero-red)}
.hero-copy{left:843px;top:421px;width:340px;font-family:"Arimo",sans-serif;font-size:12.4px;line-height:15px;color:#333}
.hero-button{left:843px;top:498px;width:165px;height:37px;background:var(--ink);color:var(--white);font-family:"Cabin",sans-serif;font-weight:600;font-size:12px;line-height:37px;text-align:center;text-decoration:none}
.slider-dots{left:843px;top:583px;display:flex;gap:8px}
.slider-dot{width:18px;height:18px;border:1.5px solid var(--brand-orange);border-radius:50%}
.slider-dot.is-current{background:var(--brand-orange)}
.slider-arrow{top:263px;width:32px;height:32px;background:#d4d4d4;display:flex;align-items:center;justify-content:center}

/* features */
.feature{top:786px;width:400px;height:467px}
.feature-divider{top:800px;width:1px;height:445px;background:#eee}
.feature-icon{position:absolute;left:0;top:32px}
.feature-title{position:absolute;left:0;top:96px;font-weight:300;font-size:30px;color:#444}
.feature-kicker{position:absolute;left:0;top:158px;width:300px;font-family:"Arimo",sans-serif;font-size:20px;line-height:28px;color:var(--accent-red);text-transform:uppercase}
.feature-rule{position:absolute;left:0;top:231px;width:276px;height:1px;background:var(--rule)}
.feature-rule i{position:absolute;left:0;top:0;width:38px;height:2px;background:#f07f87}
.feature-text{position:absolute;left:0;top:257px;width:285px;font-family:"Roboto",sans-serif;font-size:14.3px;line-height:23px;color:var(--text-grey)}
.feature-text.is-rose{color:var(--text-rose)}
.feature-more{position:absolute;left:0;top:390px;width:40px;height:40px;background:var(--button-grey);display:flex;align-items:center;justify-content:center}

/* properties */
.section-title{left:41px;top:1292px;font-weight:300;font-size:31px;color:#444}
.property{top:1365px;width:353px}
.property-photo{width:353px;height:245px;border-radius:3px;box-shadow:0 3px 4px rgba(0,0,0,.12)}
.property-caption{margin-top:20px;text-align:center;font-size:13.5px;color:#444;letter-spacing:.2px}

/* location */
.location{left:0;top:1723px;width:1200px;height:376px;background:linear-gradient(135deg,#4a4f5a 0%,#3c4659 45%,#3e4e6a 70%,#3a4558 100%)}
.location-title{left:0;top:54px;width:1200px;text-align:center;font-family:"Open Sans",sans-serif;font-size:38px;color:var(--location-gold)}
.location-address{left:0;top:136px;width:1200px;text-align:center;font-size:18.5px;line-height:27px;color:var(--white)}
.location-phones{left:0;top:217px;width:1200px;text-align:center;color:var(--white);line-height:36px;font-size:17px}
.location-phones b{font-weight:400;font-size:28px}

/* footer */
.site-footer{left:0;top:2099px;width:1200px;height:112px;background:var(--white)}
.footer-brand{left:28px;top:38px;width:90px;font-family:"Cabin",sans-serif;font-weight:600;font-size:10px;letter-spacing:1.5px;line-height:13px;color:var(--brand-orange);text-transform:uppercase}
.footer-link{top:50px;font-size:11px;color:#444;text-decoration:none}
.follow-label{left:1002px;top:50px;font-size:11px;color:#444}
.social-list{left:1075px;top:46px;display:flex;gap:10px}
.social-dot{width:18px;height:18px;border-radius:50%;background:#9a9a9a}
</style>
</head>
<body>

<header class="abs site-header">
  <svg class="abs header-wedge" width="130" height="103" viewBox="0 0 130 103" aria-hidden="true">
    <polygon points="0,0 130,0 130,103" fill="var(--brand-beige)"/>
  </svg>
  <div class="abs brand-name">Bramblecrest Real Estate</div>
  <nav class="abs main-nav">
    <a class="nav-item is-active" href="#">HOME</a>
    <a class="nav-item" href="#" style="left:796px">ABOUT US</a>
    <a class="nav-item" href="#" style="left:934px">SERVICES</a>
    <a class="nav-item" href="#" style="left:1088px">CONTACT</a>
  </nav>
</header>

<section class="abs hero">
  <div class="abs hero-visual" role="img" aria-label="Smiling couple sitting back to back inside a house outline with a rising arrow"></div>
  <h1 class="abs hero-title">FIND YOU PERFECT</h1>
  <h2 class="abs hero-title-strong">NEW HOME</h2>
  <h3 class="abs hero-sub"><span>Home Buyers</span> and Sellers</h3>
  <p class="abs hero-copy">Lorem ipsum dolor sit amet, consectetur adiposcing elt. Mauris fermentum dictum magna. Sed laireet aliquam leo. Ut tellus dolor,depitus eget, elementum vel,cursus eleifend, elit, Aenean auctor wisi et urna.Aliquam erat volutpat.</p>
  <a class="abs hero-button" href="#">READ MORE</a>
  <div class="abs slider-dots">
    <span class="slider-dot"></span><span class="slider-dot"></span><span class="slider-dot"></span><span class="slider-dot is-current"></span>
  </div>
  <a class="abs slider-arrow" href="#" style="left:30px" aria-label="Previous slide">
    <svg width="12" height="12" viewBox="0 0 12 12"><path d="M8 1 3 6l5 5" fill="none" stroke="#7a5a20" stroke-width="2"/></svg>
  </a>
  <a class="abs slider-arrow" href="#" style="left:1135px" aria-label="Next slide">
    <svg width="12" height="12" viewBox="0 0 12 12"><path d="M4 1l5 5-5 5" fill="none" stroke="#7a5a20" stroke-width="2"/></svg>
  </a>
</section>

<div class="abs feature-divider" style="left:447px"></div>
<div class="abs feature-divider" style="left:842px"></div>

<article class="abs feature" style="left:68px">
  <svg class="feature-icon" width="36" height="44" viewBox="0 0 36 44" aria-hidden="true">
    <path d="M6 40C-2 26 6 8 28 2c4 18-4 34-22 38z" fill="#222"/>
    <path d="M8 38C12 28 18 18 26 8" stroke="#fff" stroke-width="2" fill="none"/>
  </svg>
  <h3 class="feature-title">New Services</h3>
  <p class="feature-kicker">Miuas kiuasya niuyas bytrasas miaser</p>
  <div class="feature-rule"></div>
  <p class="feature-text">Bertarsa atunteger rutrum livese aserasey yoleacnrit ma hasesera deyuas lety mertasi betyudes. Cum sonatoqu eagnis ulmuese. Seugiata lesuada lecenas. Destres phaleda tyfenanec sit amm easer erment.</p>
  <a class="feature-more" href="#" aria-label="More">
    <svg width="12" height="12" viewBox="0 0 12 12"><path d="M2 2l8 8M10 4v6H4" fill="none" stroke="#fff" stroke-width="1.5"/></svg>
  </a>
</article>

<article class="abs feature" style="left:467px">
  <svg class="feature-icon" width="46" height="44" viewBox="0 0 46 44" aria-hidden="true">
    <g fill="#222">
      <ellipse cx="23" cy="10" rx="5" ry="10"/>
      <ellipse cx="23" cy="10" rx="5" ry="10" transform="rotate(72 23 23)"/>
      <ellipse cx="23" cy="10" rx="5" ry="10" transform="rotate(144 23 23)"/>
      <ellipse cx="23" cy="10" rx="5" ry="10" transform="rotate(216 23 23)"/>
      <ellipse cx="23" cy="10" rx="5" ry="10" transform="rotate(288 23 23)"/>
    </g>
  </svg>
  <h3 class="feature-title">Eco Materials</h3>
  <p class="feature-kicker">Kiuasya niuyas musers miaser bytras</p>
  <div class="feature-rule"><i></i></div>
  <p class="feature-text is-rose">Dutrum losasjha vesfaserasey yoler ma hasesera dyuas lety mert betyudes. Cumes socis natoqu eagnis dulmuese. Seugisuada lecenas. Destricies phaledatyfenanec sit amm ser ermentertya.</p>
  <a class="feature-more" href="#" aria-label="More">
    <svg width="12" height="12" viewBox="0 0 12 12"><path d="M2 2l8 8M10 4v6H4" fill="none" stroke="#fff" stroke-width="1.5"/></svg>
  </a>
</article>

<article class="abs feature" style="left:867px">
  <svg class="feature-icon" width="32" height="44" viewBox="0 0 32 44" aria-hidden="true">
    <path d="M16 2C7 2 2 9 2 16c0 7 6 10 7 17h14c1-7 7-10 7-17 0-7-5-14-14-14z" fill="#222"/>
    <rect x="9" y="35" width="14" height="3" fill="#222"/>
    <rect x="10" y="39.5" width="12" height="3" rx="1.5" fill="#222"/>
  </svg>
  <h3 class="feature-title">Top Articles</h3>
  <p class="feature-kicker">Laisasau diasya ferros ceiuasaser</p>
  <div class="feature-rule"><i></i></div>
  <p class="feature-text is-rose">Setraestricies phaledaty fenaneci ames aser erment. Ut tsdolordapege teleme ntiun svelursuses eleifend elinetsiet urna. Aliuam erat voluse tpatis ac turpis.Integer rutrues lacus.uisque nullratunteger rutru.</p>
  <a class="feature-more" href="#" aria-label="More">
    <svg width="12" height="12" viewBox="0 0 12 12"><path d="M2 2l8 8M10 4v6H4" fill="none" stroke="#fff" stroke-width="1.5"/></svg>
  </a>
</article>

<h2 class="abs section-title">Featured Properties</h2>

<figure class="abs property" style="left:41px">
  <div class="property-photo" role="img" aria-label="Bright modern living room with white sofa and concrete walls" style="background:linear-gradient(160deg,#e8e8e6,#b9bab6 55%,#8d8f8b)"></div>
  <figcaption class="property-caption">FUSCE EUISMOD CONSEQUAT ANTE</figcaption>
</figure>
<figure class="abs property" style="left:423px">
  <div class="property-photo" role="img" aria-label="Concrete bathroom with large window and wooden floor" style="background:linear-gradient(180deg,#3a3633 0%,#8c8a86 40%,#c9c8c4 55%,#8a5a3a 85%,#6e4428)"></div>
  <figcaption class="property-caption">FUSCE EUISMOD CONSEQUAT ANTE</figcaption>
</figure>
<figure class="abs property" style="left:803px">
  <div class="property-photo" role="img" aria-label="Landscaped garden terrace with pergola and white fence" style="background:linear-gradient(180deg,#b9cfe0 0%,#6f8f4a 35%,#e8e6e2 60%,#7c9a48 100%)"></div>
  <figcaption class="property-caption">FUSCE EUISMOD CONSEQUAT ANTE</figcaption>
</figure>

<section class="abs location" role="img" aria-label="Dark city map of the office surroundings">
  <h2 class="abs location-title">Location</h2>
  <p class="abs location-address">412 Larkfield Lane<br>Norbridge, NB7 2QL.</p>
  <p class="abs location-phones">Freephone:<b>+1 800 555 0142</b><br>Telephone:<b>+1 555 603 0199</b></p>
</section>

<footer class="abs site-footer">
  <div class="abs footer-brand">Bramblecrest Real Estate</div>
  <a class="abs footer-link" href="#" style="left:127px">About us</a>
  <a class="abs footer-link" href="#" style="left:203px">Our services</a>
  <a class="abs footer-link" href="#" style="left:296px">Agents</a>
  <a class="abs footer-link" href="#" style="left:363px">Blog</a>
  <a class="abs footer-link" href="#" style="left:417px">Contacts</a>
  <span class="abs follow-label">Follow us:</span>
  <div class="abs social-list">
    <span class="social-dot"></span><span class="social-dot"></span><span class="social-dot"></span><span class="social-dot"></span>
  </div>
</footer>

</body>
</html>
```